Dynamic Website Design For Dynamic Speaker and Business Coach!

Professional Website Design for a for a Professional Business coach, Business trainer, and Speaker.

Note: This is for design only. No coding required. We want to see your ideas for a great website! This will be a FUN design and not boring like others you may work on.

Please let your creative ideas flow. We have given you a ton of info along with videos to help you understand what we are after, however we WANT your creativity to shine through in your designs!

We are a professional company that has run hundreds of crowdsourced projects on multiple platforms. If you participate in this contest (we hope you do) you can expect great video feedback, consistent feedback, and also our guarantee that if we know your website design will not be what we are looking for we will notify you so you don’t waste your time if there is no chance of you winning.

We respect and recognize this is how you make your living and we will not play games. We look forward to an awesome contest and awesome website designs.

Design Brief:

We are looking for a fresh and fun new design for

http://www.grovepath7.net

This individual (Dana Wilcox) teaches and trains corporations and businesses in the fields of leadership, sales, communication, business operations etc. Additionally this business teaches and mentors business professionals in a small group level or 1 on 1.

The website needs to convey trust, professionalism, and affluent, while at the same time having some personality!

This business operates on 3 core principles that we would like to see incorporated into the logo if it is a good fit. The 3 principals are:

Focus
Accountability
Results

Here is a video to help explain what we like about the current site and what we don’t like:
http://clipvault.example/t/Qm7rTpLw2xKa

As you can see the website is geared towards business professionals. Please look over the website to learn what they do. Obviously this is not a good website so we need your help.

We want a website that is professional-looking, has personality and is geared more towards promoting Dana Wilcox, the owner of Grovepath 7 Partners as a Speaker and Business Consultant. The more you can incorporate clean, professional and fun personality elements into the design, the better off you are at winning.

Here are some examples of other sites in their business that have some things we like:

http://hemlineplays.example Please watch video to learn what we like and don’t like:
http://clipvault.example/t/NrpW3kTyvQa

http://tallpinepromo.example Please watch video to learn what we like and don’t like:
http://clipvault.example/t/K9wPzmRu

http://www.marlaquint.example Please watch video to learn what we like and don’t like:
http://clipvault.example/t/Vx2pq7N5a81

http://www.dwl7z.example Please watch video to learn what we like and don’t like:
http://clipvault.example/t/8K3wuhTzbnx

NOTE: We do not want to copy anything outright. We want to learn, model and take their ideas and make them better. We also want to be flexible and take what we like along with your creativity to make an amazing design.

Here is what we are looking for in more specific terms:

Colors: We like the darker blue (not the light blue like the site) and also a burnt orange. I’ve attached her Logo so you can get an idea and feel for the colors.

When looking at colors please know that the current site and look is NOT what we are going for. We are going for a clean and professional look but also a look that is BOLD, FUN, and Vibrant (hence the colors).

Menu: Horizontal. We like bold and easy to read menu items. Don’t make it small and cluttered.

Site Structure: Clean and easy to navigate. We have a lot of content to display so we need a clean structure that breaks up the text and content areas.
Images: Please pull images from the current site. We can always replace the images of course, but if you show them “their own stuff” in the new design you will be closer to winning because it will feel more like “them”

Look and Feel: Professional. Fun. High-End. Business-like. This website needs to convey that Dana Wilcox and Grovepath 7 Partners are professional. That Dana Wilcox is a sought-after Speaker and Business Consultant who knows what she is talking about; can be serious when she needs to be, but also likes to have fun with her clients. This site must convey that!

Content Areas: It is a safe bet that if it is on the current site we need it on the new site. So don’t drop anything as it makes it hard to “cut content”.

What we don't want: We do not want clutter, boring, or templates or themes. We don’t want too cartoony, too cute, or too fancy… Be creative!

Out of respect to professional designers who really are working hard to win if you do not follow this brief, you submit worn out themes, templates, or boring designs you will be eliminated. We are offering great prize money for this so we expect great visual designs.

Reason: Our client is out of town, and waiting to hear feedback from them. So, in the meantime, we wanted to keep the project going to see what else you designers can come up with. As soon as we hear back from our client, we will pass along the info. Thanks!

Target Market(s)

Target Audience is entrepreneurs and business professionals alike. This is all business to business stuff.

This person teaches and trains startups and billion dollar companies. The common thread is that they are all businesses and companies who need help in various areas including sales, communication, business operations, etc.

Industry/Entity Type

Business

Font styles to use
Sans Serif

Requirements
Must have
• Brief is very detailed. Please review
Nice to have
Should not have

```html
<!DOCTYPE html>
<html lang="en">
<head>
<meta charset="utf-8">
<title>Grovepath 7 Partners – Business Coaching and Consulting</title>
<link rel="stylesheet" href="https://fonts.googleapis.com/css2?family=Mulish:wght@400;600;700&family=Open+Sans:ital,wght@0,400;0,600;0,700;1,400&family=DM+Serif+Display&display=swap">
<style>
:root{
  --navy:#0b2d83;
  --navy-deep:#062a78;
  --orange:#d98a2c;
  --orange-bright:#ef8f2a;
  --orange-dark:#a9621f;
  --nav-top:#e39a45;
  --nav-bottom:#c2722a;
  --check:#f2a81d;
  --text:#666;
  --text-dark:#222;
  --panel:#f2f2f2;
  --line:#ddd;
  --white:#fff;
}
*{margin:0;padding:0;box-sizing:border-box}
html,body{width:730px;height:1200px;overflow:hidden;background:var(--white)}
body{position:relative;font-family:"Open Sans",Arial,sans-serif;color:var(--text)}
.abs{position:absolute}

/* header */
.brand{left:75px;top:26px;display:flex;align-items:center;gap:8px}
.brand-mark{width:22px;height:22px;border-radius:50%;background:var(--orange)}
.brand-name{font-family:"Mulish",sans-serif;font-weight:700;font-size:20px;color:var(--navy);letter-spacing:-.2px}
.contact-now{right:93px;top:35px;font-family:"Mulish",sans-serif;font-size:10px;color:var(--navy)}
.phone{right:80px;top:48px;font-family:"Mulish",sans-serif;font-size:15.5px;color:var(--navy);font-weight:600}
.social{left:490px;top:55px;display:flex;gap:3px}
.social span{width:12px;height:12px;display:block}
.social span:nth-child(1){background:#b8322a}
.social span:nth-child(2){background:#3b5998}
.social span:nth-child(3){background:#ee8a26}

/* nav */
.nav{left:0;top:78px;width:730px;height:32px;background:linear-gradient(var(--nav-top),var(--nav-bottom))}
.nav ul{list-style:none;display:flex;gap:11px;padding-left:83px;line-height:32px}
.nav li{font-family:"Mulish",sans-serif;font-size:9.4px;color:var(--white);font-weight:400;letter-spacing:.1px}

/* hero */
.hero{left:67px;top:110px;width:596px;height:264px;border:1px solid #e4e4e4;background:var(--white);overflow:hidden}
.hero-photo{left:200px;top:0;width:395px;height:263px;
  background:
    linear-gradient(90deg,#fff 0%,rgba(255,255,255,0) 22%),
    linear-gradient(180deg,rgba(255,255,255,.55) 0%,rgba(255,255,255,0) 30%,rgba(40,40,50,.18) 100%),
    linear-gradient(90deg,#e9e6e2 10%,#b58d78 26%,#e6e9ef 40%,#f3ece4 52%,#9fb6d6 68%,#c4d2e6 78%,#e8c9c3 90%,#d9d1cc 100%)}
.hero-title{left:49px;top:109px;font-family:"Mulish",sans-serif;font-size:16.5px;line-height:23px;font-weight:600;text-transform:uppercase;letter-spacing:.1px}
.hero-title .l1{color:var(--navy);display:block}
.hero-title .l2{color:var(--orange);display:block}
.hero-text{left:40px;top:135px;width:225px;font-size:7.6px;line-height:13px;color:#777}
.hero-dots{left:39px;top:171px;display:flex;gap:3px}
.hero-dots span{width:7px;height:7px;border-radius:50%;background:#999}

/* intro */
.intro-title{left:67px;top:408px;font-family:"Mulish",sans-serif;font-weight:400;font-size:16px;color:var(--orange)}
.coach-photo{left:69px;top:438px;width:82px;height:96px;
  background:
    radial-gradient(ellipse 30px 34px at 50% 42%,#d9a98c 0%,#b57c60 55%,rgba(90,50,35,0) 100%),
    linear-gradient(180deg,#6d8fae 0%,#5a7d9e 55%,#1e1e22 78%,#7fa9c4 100%)}
.intro-copy{left:161px;top:436px;width:288px;font-size:7.4px;line-height:12.8px;color:#777}
.intro-copy p+p{margin-top:6px}
.sub-title{left:69px;top:557px;font-family:"Mulish",sans-serif;font-weight:400;font-size:12.6px;color:var(--navy)}
.checks{left:70px;top:583px;list-style:none}
.checks li{display:flex;align-items:center;gap:7px;height:17px;font-size:7.6px;color:#555}
.checks svg{width:12px;height:12px;flex:none}
.closing{left:71px;top:674px;width:385px;font-size:7.6px;line-height:14px;color:#777}
.divider{left:69px;top:721px;width:386px;height:1px;background:var(--line)}

/* cards */
.card{top:742px;width:181px}
.card-img{width:181px;height:82px}
.card h3{font-family:"Open Sans",sans-serif;font-weight:400;font-size:12.5px;margin-top:9px;line-height:16px}
.card h4{font-family:"Open Sans",sans-serif;font-weight:400;font-size:10px;line-height:15px}
.card p{font-size:7.4px;line-height:12.7px;color:#777;margin-top:3px}
.card p+p{margin-top:2px}
.btn{display:inline-block;margin-top:10px;width:60px;height:18px;line-height:18px;text-align:center;font-size:6.6px;font-weight:700;color:var(--white);border-radius:2px}
.card-a{left:71px}
.card-a .card-img{background:
    linear-gradient(180deg,rgba(255,255,255,.6) 0%,rgba(255,255,255,0) 45%),
    linear-gradient(90deg,#eef1f4 0%,#c9b1a0 22%,#f4f4f5 38%,#8a6a58 52%,#e7d3c5 66%,#f2f2f4 80%,#c9a497 100%)}
.card-a h3,.card-a h4{color:var(--text-dark)}
.card-a .btn{background:var(--navy)}
.card-b{left:271px}
.card-b .card-img{background:
    linear-gradient(180deg,rgba(255,255,255,.55) 0%,rgba(255,255,255,0) 40%),
    linear-gradient(90deg,#e3e8ee 0%,#d7b49b 14%,#f3f3f3 26%,#5d4a40 42%,#9db4cf 56%,#eceff3 70%,#7f93ad 86%,#d8ccc3 100%)}
.card-b h3,.card-b h4{color:var(--navy)}
.card-b .btn{background:var(--orange-bright)}

/* sidebar */
.signup{left:480px;top:404px;width:183px;height:181px;background:var(--panel);border:1px solid #e8e8e8}
.signup h3{font-family:"Mulish",sans-serif;font-weight:400;font-size:11.4px;line-height:16px;color:#555;text-align:center;margin-top:18px}
.signup label{display:block;font-size:7px;color:#555;margin:10px 0 3px 18px}
.signup label:first-of-type{margin-top:12px}
.signup .field{display:block;margin-left:17px;width:151px;height:19px;background:var(--white);border:1px solid #e4e4e4}
.signup .submit{display:block;margin:8px 0 0 17px;width:151px;height:24px;background:var(--orange-bright);color:var(--white);text-align:center;line-height:24px;font-family:"Mulish",sans-serif;font-size:10.5px;font-weight:400}
.video{left:480px;top:592px;width:183px;height:121px;overflow:hidden;
  background:linear-gradient(90deg,#1f69a8 0%,#2e86c4 55%,#3a7fb6 68%,#b9a295 78%,#2a2c36 92%,#1d4f82 100%)}
.video-text{left:-4px;top:14px;width:150px;font-family:"DM Serif Display",Georgia,serif;font-size:22px;line-height:25px;color:var(--white);text-align:right;white-space:nowrap}
.play{left:72px;top:45px}
.testimonials{left:481px;top:724px;width:182px;height:207px;border:1px solid #ddd}
.testimonials h3{height:29px;background:var(--navy-deep);color:var(--white);font-family:"Mulish",sans-serif;font-weight:400;font-size:12.4px;line-height:29px;padding-left:19px}
.quote{padding:0 18px 0 20px}
.quote p{font-style:italic;font-size:7px;line-height:11.6px;color:#888;margin-top:13px}
.quote cite{display:block;font-style:normal;font-size:7px;color:#222;margin-top:5px;font-weight:600}
.quote+.quote p{margin-top:15px}

/* footer */
.footer{left:0;top:1000px;width:730px;height:164px;background:linear-gradient(#d78a3a,#c8782c)}
.foot-col{top:1035px;color:var(--white)}
.foot-col h4{font-family:"Mulish",sans-serif;font-weight:400;font-size:11.6px;text-transform:uppercase;margin-bottom:4px}
.foot-col li{list-style:none;font-size:7.6px;line-height:14px}
.foot-col p{font-size:7.6px;line-height:14px}
.col-links{left:75px}
.col-res{left:180px}
.col-contact{left:289px}
.col-news{left:417px}
.email-field{display:block;width:149px;height:18px;background:var(--white);margin-top:4px;font-size:7px;color:#777;line-height:18px;padding-left:7px}
.subscribe{display:block;margin-top:6px;width:70px;height:18px;background:var(--navy);color:var(--white);font-size:7.6px;font-weight:700;text-align:center;line-height:18px}
.bottom-bar{left:0;top:1164px;width:730px;height:36px;background:var(--orange-dark)}
.copyright{left:76px;top:1176px;font-size:7px;color:var(--white)}
</style>
</head>
<body>

<header>
  <div class="abs brand"><span class="brand-mark"></span><span class="brand-name">Grovepath 7 Partners</span></div>
  <div class="abs social" aria-label="Social links"><span></span><span></span><span></span></div>
  <div class="abs contact-now">Contact Us Now</div>
  <div class="abs phone">(505) 418-2276</div>
</header>

<nav class="abs nav">
  <ul>
    <li>PASSION</li><li>WHO WE ARE</li><li>SPEAKER</li><li>FREE VIDEO</li><li>WEB TV SHOW</li><li>TESTIMONIALS</li><li>RIDGEWAY LEARNING</li><li>BLOG</li><li>CONTACT</li>
  </ul>
</nav>

<section class="abs hero">
  <div class="abs hero-photo" role="img" aria-label="Photo of a smiling business team standing together in a bright office"></div>
  <h1 class="abs hero-title" style="left:40px;top:86px"><span class="l1">Albuquerque Business</span><span class="l2">Coaching and Consulting</span></h1>
  <p class="abs hero-text">Morbi ornare gravida elit Integer congue augue et malesu ada iaculis ipsum dui aliquet felis at cursu</p>
  <div class="abs hero-dots"><span></span><span></span><span></span><span></span></div>
</section>

<main>
  <h2 class="abs intro-title">Albuquerque Business Coaching and Consulting</h2>
  <div class="abs coach-photo" role="img" aria-label="Portrait photo of the business coach"></div>
  <div class="abs intro-copy">
    <p>Are you searching to bridge the gap between where you are and where you want to be? As you face greater pressure to “move the needle” on your company’s productivity and bottom line profitability, how prepared are you to step in and shine as the leader?We specialize in guiding leaders to become easier to follow.&nbsp; You’re in the Right Place.</p>
    <p>Mauris vel lacus vitae felis vestibulum volutpat Etiam est nunc venenatis in tris-tique eu imperdiet ac nisl Cum sociis natoque penatibus et magnis</p>
  </div>

  <h2 class="abs sub-title">Albuquerque Business Coach: Focus, Accountability, &amp; Results</h2>
  <ul class="abs checks">
    <li><svg viewBox="0 0 12 12"><circle cx="6" cy="6" r="6" fill="var(--check)"/><path d="M3.2 6.2l1.9 1.9 3.8-3.9" stroke="#fff" stroke-width="1.4" fill="none"/></svg>Development Of An Operational Plan That Links All Departments</li>
    <li><svg viewBox="0 0 12 12"><circle cx="6" cy="6" r="6" fill="var(--check)"/><path d="M3.2 6.2l1.9 1.9 3.8-3.9" stroke="#fff" stroke-width="1.4" fill="none"/></svg>Implementation And Monitoring Individual And Departmental Plans</li>
    <li><svg viewBox="0 0 12 12"><circle cx="6" cy="6" r="6" fill="var(--check)"/><path d="M3.2 6.2l1.9 1.9 3.8-3.9" stroke="#fff" stroke-width="1.4" fill="none"/></svg>Diagnosing Employee Training Needs</li>
    <li><svg viewBox="0 0 12 12"><circle cx="6" cy="6" r="6" fill="var(--check)"/><path d="M3.2 6.2l1.9 1.9 3.8-3.9" stroke="#fff" stroke-width="1.4" fill="none"/></svg>Delivering The Training To Develop Leaders And Staff</li>
    <li><svg viewBox="0 0 12 12"><circle cx="6" cy="6" r="6" fill="var(--check)"/><path d="M3.2 6.2l1.9 1.9 3.8-3.9" stroke="#fff" stroke-width="1.4" fill="none"/></svg>Coach Leaders, Individuals And Teams</li>
  </ul>
  <p class="abs closing">Whether you’re leading a company, or are an employee, all of us have a role to play in contributing to the profit and the future of the company.</p>
  <div class="abs divider"></div>

  <article class="abs card card-a">
    <div class="card-img" role="img" aria-label="Photo of colleagues meeting around a table"></div>
    <h3>Your organization expects</h3>
    <h4>you to deliver value by delivering</h4>
    <p>Mauris vel lacus vitae felis vestibulum volutpat Etiam est nunc venenatis in tristique eu imperdiet ac nisl Cum sociis natoque penatibus et magnis dis parturient montes nascetur ridicu</p>
    <span class="btn">READ MORE</span>
  </article>
  <article class="abs card card-b">
    <div class="card-img" role="img" aria-label="Photo of a team reviewing documents together"></div>
    <h3>Grovepath 7 Partners has</h3>
    <h4>delivered on our promise.</h4>
    <p>Mauris vel lacus vitae felis vestibulum volutpat Etiam est nunc venenatis in tristique</p>
    <p>Eu imperdiet ac nisl Cum sociis natoque penatibus et magnis dis parturient montes nascetur</p>
    <span class="btn">READ MORE</span>
  </article>
</main>

<aside>
  <form class="abs signup">
    <h3>Sign up for my FREE report<br>"Have Fun While</h3>
    <label>First Name</label><span class="field"></span>
    <label>Last Name</label><span class="field"></span>
    <span class="submit">SUBMIT NOW</span>
  </form>
  <div class="abs video" role="img" aria-label="Video preview: the coach speaking beside the question about focus, accountability and results">
    <p class="abs video-text">You Need<br>More Focus,<br>Accountability<br>&amp; Results?</p>
    <svg class="abs play" width="38" height="38" viewBox="0 0 38 38"><circle cx="19" cy="19" r="14" fill="#fff"/><path d="M16 13v12l9-6z" fill="#111"/></svg>
  </div>
  <section class="abs testimonials">
    <h3>Testimonials</h3>
    <div class="quote"><p>Morbi porta libero id ullamcorper non-ummy nibh ligula pulvinar metus eget consectetuer augue nisi quis lacus Ut ac mi quis lacus mollis aliquam Curabitur iaculis tempus eros Curabitur vel mi sit</p><cite>By Author Name</cite></div>
    <div class="quote"><p>Etiam est nunc venenatis in tristique eu imperdiet ac nisl Cum sociis natoque penatibus et magnis dis parturient montes nascetur ridiculus mus in iaculis</p><cite>By Author Name</cite></div>
  </section>
</aside>

<footer>
  <div class="abs footer"></div>
  <div class="abs foot-col col-links"><h4>Quick Links</h4><ul><li>Passion</li><li>Who We Are</li><li>Speaker</li><li>Free Video</li><li>Web TV Show</li></ul></div>
  <div class="abs foot-col col-res"><h4>Resources</h4><ul><li>Testimonials</li><li>Ridgeway Learning</li><li>Blog</li><li>Contact</li></ul></div>
  <div class="abs foot-col col-contact"><h4>Contact</h4><p>42 Alder Lane Suite 3B<br>Fairview 10388 TX<br>586.410.7731<br>hello@grovepath7.net</p></div>
  <div class="abs foot-col col-news"><h4>Newsleters Sign Up</h4><p>Please sign up here for latest offers.</p><span class="email-field">email address</span><span class="subscribe">SUBSCRIBE</span></div>
  <div class="abs bottom-bar"></div>
  <p class="abs copyright">© 2014 Company Name&nbsp; All right reserved&nbsp; Term of Use</p>
</footer>

</body>
</html>
```